Engineering/Manufacturing Company Needs PowerPoint Update and Template

We want to update the look and feel of our current corporate overview PowerPoint. We would like a working template moving forward with 6-8 slide layouts as well as a couple cover page options. Our content ranges from basic bullet points to complex graphs, images, and a combination of those, so we need templates that will work with a wide variety of content.
Our company specializes in complex precision machining, Engineering, and Advanced heavy duty truck products. We would like this presentation to represent our high-level manufacturing technology.
Our corporate color is blue (RBG 26/75/159), and we also use gray and white. We are looking for a modern, clean, yet masculine/industrial feeling. I have included our company logo, but other than that we would like to see what you can come up with. We would like it to feel clean yet industrial.
Target Market(s)
High-level management in the manufacturing and heavy duty truck/bus industries.
Industry/Entity Type
Manufacturer

```html
<!DOCTYPE html>
<html lang="en">
<head>
<meta charset="utf-8">
<title>Norvane – Presentation Template Overview</title>
<link href="https://fonts.googleapis.com/css2?family=Lato:ital,wght@0,400;0,700;0,900;1,400&display=swap" rel="stylesheet">
<style>
  :root{
    --blue:#1a4b9f;
    --blue-dark:#163f86;
    --steel:#5a6f96;
    --gray:#8a8f99;
    --gray-light:#c9ccd3;
    --paper:#eef0f6;
    --board:#e9e9ea;
    --ink:#6d7280;
    --white:#ffffff;
  }
  *{margin:0;padding:0;box-sizing:border-box}
  html,body{width:1200px;height:1200px;overflow:hidden;background:var(--board);font-family:"Lato",sans-serif}
  .board{position:relative;width:1200px;height:1200px}
  .slide{position:absolute;width:144px;height:82px;box-shadow:0 1px 3px rgba(0,0,0,.28);display:block}
  .slide.lg{width:148px;height:84px}
  .st{font:900 4.6px "Lato",sans-serif;fill:var(--blue)}
  .stw{font:900 4.6px "Lato",sans-serif;fill:var(--white)}
  .sx{font:400 2.5px "Lato",sans-serif;fill:var(--ink)}
  .sxw{font:400 2.5px "Lato",sans-serif;fill:#dfe6f3}
  .sh{font:700 2.9px "Lato",sans-serif;fill:#3b4252}
  .shw{font:700 2.9px "Lato",sans-serif;fill:var(--white)}
  .big{font:900 7px "Lato",sans-serif;fill:var(--white)}
  .brand{font:900 6px "Lato",sans-serif;fill:var(--blue)}

  /* hero cover */
  .hero{position:absolute;left:102px;top:62px;width:388px;height:216px;
    background:linear-gradient(120deg,#1a4b9f 0%,#2f5ea8 35%,#6f8fbd 62%,#c4a98e 85%,#dcc0a0 100%);
    box-shadow:0 2px 6px rgba(0,0,0,.3);overflow:hidden}
  .hero-photo{position:absolute;inset:0;background:linear-gradient(180deg,rgba(26,75,159,0) 40%,rgba(22,63,134,.75) 100%)}
  .hero-badge{position:absolute;left:16px;top:21px;width:194px;height:74px;background:var(--white);border-radius:9px;
    display:flex;align-items:center;justify-content:center}
  .hero-badge span{font:900 34px "Lato",sans-serif;color:var(--blue);letter-spacing:1px}
  .hero-title{position:absolute;left:29px;top:155px;font:900 19px "Lato",sans-serif;color:var(--white)}
  .hero-text{position:absolute;left:29px;top:181px;width:220px;font:italic 400 5.2px/1.8 "Lato",sans-serif;color:#e6ecf6}

  /* widescreen display panel */
  .display{position:absolute;left:40px;top:350px;width:514px;height:290px;background:#f4f4f5;box-shadow:0 1px 4px rgba(0,0,0,.15)}
  .display-label{position:absolute;left:340px;top:14px;width:150px;height:60px;border:1px solid #777;
    display:flex;align-items:center;justify-content:center;text-align:center;font:400 11px/1.3 "Lato",sans-serif;color:#333;letter-spacing:.5px}

  .heading{position:absolute;font:700 16px "Lato",sans-serif;color:var(--blue);text-align:center;width:400px}
  .cont{position:absolute;left:494px;top:1162px;font:700 15px "Lato",sans-serif;color:var(--blue)}
  .cont-arrow{position:absolute;left:538px;top:1160px}
</style>
</head>
<body>
<svg width="0" height="0" style="position:absolute" aria-hidden="true">
  <defs>
    <linearGradient id="gPhoto" x1="0" y1="0" x2="1" y2="1">
      <stop offset="0" stop-color="#1f3f78"/><stop offset=".55" stop-color="#5f7aa6"/><stop offset="1" stop-color="#b7c2d6"/>
    </linearGradient>
    <linearGradient id="gWarm" x1="0" y1="0" x2="1" y2="1">
      <stop offset="0" stop-color="#28467e"/><stop offset=".6" stop-color="#7b8aa5"/><stop offset="1" stop-color="#c9a27c"/>
    </linearGradient>
    <linearGradient id="gSteel" x1="0" y1="0" x2="1" y2="0">
      <stop offset="0" stop-color="#6b7483"/><stop offset="1" stop-color="#c3c8d1"/>
    </linearGradient>
    <linearGradient id="gCover" x1="0" y1="0" x2="1" y2="1">
      <stop offset="0" stop-color="#1a4b9f"/><stop offset=".6" stop-color="#3f68ad"/><stop offset="1" stop-color="#8aa2c7"/>
    </linearGradient>
    <g id="fr">
      <rect width="144" height="82" fill="#eef0f6"/>
      <text x="139" y="8" text-anchor="end" font-family="Lato,sans-serif" font-weight="900" font-size="5.4" fill="#1a4b9f">NORVANE</text>
      <rect y="79" width="144" height="3" fill="#1a4b9f"/>
      <rect x="118" y="79" width="26" height="3" fill="#8a8f99"/>
    </g>
    <g id="tile">
      <rect width="20" height="20" fill="#c9ccd3"/>
    </g>
  </defs>
</svg>

<main class="board">

  <!-- cover -->
  <section class="hero">
    <div class="hero-photo" role="img" aria-label="Industrial plant pipework photo in blue tones"></div>
    <div class="hero-badge"><span>NORVANE</span></div>
    <h1 class="hero-title">PRESENTATION TITLE</h1>
    <p class="hero-text">Lorem Ipsum is simply dummy text of the printing and typesetting industry. Lorem Ipsum has been the industry's standard dummy text ever since the 1500s.</p>
  </section>

  <!-- widescreen display -->
  <section class="display">
    <div class="display-label">16:9 WIDESCREEN<br>DISPLAY</div>

    <svg class="slide" style="left:14px;top:14px;width:150px;height:84px" viewBox="0 0 144 82">
      <rect width="144" height="82" fill="url(#gCover)" role="img" aria-label="Industrial plant photo"/>
      <rect x="10" y="10" width="52" height="20" rx="3" fill="#fff"/>
      <text x="36" y="22.5" text-anchor="middle" class="brand">NORVANE</text>
      <text x="10" y="60" class="big">PRESENTATION TITLE</text>
    </svg>
    <svg class="slide" style="left:178px;top:14px;width:150px;height:84px" viewBox="0 0 144 82">
      <use href="#fr"/><text x="5" y="8" class="st">YOUR SLIDE TITLE HERE</text>
      <rect x="0" y="14" width="60" height="40" fill="url(#gPhoto)" role="img" aria-label="Machining photo"/>
      <text x="70" y="30" class="sh">"If you don't know where you</text>
      <text x="70" y="35" class="sh">are going, you'll end up</text>
      <text x="70" y="40" class="sh">someplace else."</text>
    </svg>

    <svg class="slide" style="left:14px;top:108px;width:150px;height:84px" viewBox="0 0 144 82">
      <use href="#fr"/><text x="5" y="8" class="st">YOUR SLIDE TITLE HERE</text>
      <g fill="#1a4b9f"><rect x="10" y="42" width="6" height="30"/><rect x="30" y="32" width="6" height="40"/><rect x="50" y="48" width="6" height="24"/><rect x="70" y="26" width="6" height="46"/><rect x="90" y="38" width="6" height="34"/><rect x="110" y="30" width="6" height="42"/></g>
      <g fill="#8a8f99"><rect x="17" y="50" width="6" height="22"/><rect x="37" y="44" width="6" height="28"/><rect x="57" y="40" width="6" height="32"/><rect x="77" y="52" width="6" height="20"/><rect x="97" y="46" width="6" height="26"/><rect x="117" y="54" width="6" height="18"/></g>
    </svg>
    <svg class="slide" style="left:178px;top:108px;width:150px;height:84px" viewBox="0 0 144 82">
      <use href="#fr"/><text x="5" y="8" class="st">YOUR SLIDE TITLE HERE</text>
      <rect x="6" y="16" width="40" height="26" fill="url(#gPhoto)" role="img" aria-label="Turbine photo"/>
      <rect x="50" y="16" width="40" height="26" fill="url(#gWarm)" role="img" aria-label="Truck photo"/>
      <rect x="94" y="16" width="44" height="26" fill="url(#gSteel)" role="img" aria-label="Gear photo"/>
      <text x="6" y="50" class="sx">Lorem ipsum dolor sit amet consectetur.</text>
      <text x="6" y="55" class="sx">Sed do eiusmod tempor incididunt.</text>
    </svg>
    <svg class="slide" style="left:342px;top:108px;width:150px;height:84px" viewBox="0 0 144 82">
      <use href="#fr"/><text x="5" y="8" class="st">ICON SLIDE IDEA</text>
      <g fill="#1a4b9f"><rect x="10" y="20" width="8" height="8" rx="1"/><rect x="10" y="38" width="8" height="8" rx="1"/><rect x="10" y="56" width="8" height="8" rx="1"/><rect x="76" y="20" width="8" height="8" rx="1"/><rect x="76" y="38" width="8" height="8" rx="1"/><rect x="76" y="56" width="8" height="8" rx="1"/></g>
      <text x="22" y="25" class="sh">Title Goes Here</text><text x="22" y="43" class="sh">Title Goes Here</text><text x="22" y="61" class="sh">Title Goes Here</text>
      <text x="88" y="25" class="sh">Title Goes Here</text><text x="88" y="43" class="sh">Title Goes Here</text><text x="88" y="61" class="sh">Title Goes Here</text>
    </svg>

    <svg class="slide" style="left:14px;top:202px;width:150px;height:84px" viewBox="0 0 144 82">
      <use href="#fr"/><text x="5" y="8" class="st">YOUR SLIDE TITLE HERE</text>
      <path d="M10 72 L10 56 L30 40 L50 52 L70 30 L90 48 L110 36 L134 58 L134 72 Z" fill="#8ea3cc"/>
      <path d="M10 72 L10 62 L30 54 L50 62 L70 46 L90 60 L110 52 L134 66 L134 72 Z" fill="#1a4b9f"/>
    </svg>
    <svg class="slide" style="left:178px;top:202px;width:150px;height:84px" viewBox="0 0 144 82">
      <use href="#fr"/><text x="5" y="8" class="st">YOUR SLIDE TITLE HERE</text>
      <circle cx="40" cy="46" r="22" fill="#c9ccd3"/>
      <path d="M40 46 L40 24 A22 22 0 0 1 60 56 Z" fill="#1a4b9f"/>
      <circle cx="40" cy="46" r="9" fill="#eef0f6"/>
      <text x="76" y="30" class="sx">Lorem ipsum dolor sit amet, consectetur.</text>
      <text x="76" y="36" class="sx">Sed do eiusmod tempor incididunt ut.</text>
      <text x="76" y="42" class="sx">Labore et dolore magna aliqua.</text>
    </svg>
    <svg class="slide" style="left:342px;top:202px;width:150px;height:84px" viewBox="0 0 144 82">
      <use href="#fr"/><text x="5" y="8" class="st">YOUR SLIDE TITLE HERE</text>
      <g fill="#1a4b9f"><rect x="14" y="28" width="5" height="44"/><rect x="32" y="34" width="5" height="38"/><rect x="50" y="24" width="5" height="48"/><rect x="68" y="40" width="5" height="32"/><rect x="86" y="30" width="5" height="42"/><rect x="104" y="44" width="5" height="28"/><rect x="122" y="36" width="5" height="36"/></g>
      <g fill="#8a8f99"><rect x="20" y="40" width="5" height="32"/><rect x="38" y="46" width="5" height="26"/><rect x="56" y="36" width="5" height="36"/><rect x="74" y="50" width="5" height="22"/><rect x="92" y="42" width="5" height="30"/><rect x="110" y="54" width="5" height="18"/><rect x="128" y="48" width="5" height="24"/></g>
    </svg>
  </section>

  <!-- title slide ideas -->
  <h2 class="heading" style="left:96px;top:684px">Title Slide Ideas</h2>

  <svg class="slide lg" style="left:54px;top:719px" viewBox="0 0 144 82">
    <rect width="144" height="82" fill="url(#gPhoto)" role="img" aria-label="Blue industrial pipework photo"/>
    <text x="136" y="16" text-anchor="end" font-family="Lato,sans-serif" font-weight="900" font-size="10" fill="#fff">NORVANE</text>
    <rect x="0" y="54" width="92" height="14" fill="#1a4b9f"/>
    <text x="8" y="63" class="stw" style="font-size:6px">PRESENTATION TITLE</text>
    <text x="8" y="73" class="sxw">Lorem ipsum is simply dummy text of the printing.</text>
  </svg>
  <svg class="slide lg" style="left:226px;top:719px" viewBox="0 0 144 82">
    <rect width="144" height="82" fill="url(#gWarm)" role="img" aria-label="Industrial plant photo with warm light"/>
    <rect x="6" y="6" width="56" height="22" rx="3" fill="#fff"/>
    <text x="34" y="19.5" text-anchor="middle" class="brand">NORVANE</text>
    <text x="10" y="62" class="stw" style="font-size:6px">PRESENTATION TITLE</text>
    <text x="10" y="70" class="sxw">Lorem ipsum is simply dummy text of the printing.</text>
  </svg>
  <svg class="slide lg" style="left:398px;top:719px" viewBox="0 0 144 82">
    <rect width="144" height="62" fill="url(#gCover)" role="img" aria-label="Blue machinery photo"/>
    <rect y="62" width="144" height="20" fill="#eef0f6"/>
    <rect x="40" y="14" width="64" height="20" rx="3" fill="#fff"/>
    <text x="72" y="27" text-anchor="middle" class="brand">NORVANE</text>
    <text x="72" y="48" text-anchor="middle" class="stw" style="font-size:5.5px">PRESENTATION TITLE</text>
    <text x="8" y="70" class="sx">Company name, Inc. Lorem ipsum dolor sit amet consectetur adipiscing.</text>
    <text x="8" y="74" class="sx">Sed do eiusmod tempor incididunt ut labore.</text>
  </svg>

  <!-- content slide ideas -->
  <h2 class="heading" style="left:96px;top:831px">Content Slide Ideas</h2>

  <svg class="slide lg" style="left:54px;top:860px" viewBox="0 0 144 82">
    <rect width="144" height="82" fill="#1a4b9f"/>
    <text x="12" y="24" font-family="Lato,sans-serif" font-weight="900" font-size="14" fill="#fff">“</text>
    <text x="22" y="26" class="sxw">Lorem ipsum dolor sit amet, consectetur adipiscing elit, sed do</text>
    <text x="22" y="31" class="sxw">eiusmod tempor incididunt ut labore et dolore magna aliqua.</text>
    <text x="22" y="36" class="sxw">Ut enim ad minim veniam, quis nostrud exercitation ullamco.</text>
    <text x="22" y="41" class="sxw">Duis aute irure dolor in reprehenderit in voluptate.</text>
    <text x="124" y="62" font-family="Lato,sans-serif" font-weight="900" font-size="14" fill="#fff">”</text>
  </svg>
  <svg class="slide lg" style="left:226px;top:860px" viewBox="0 0 144 82">
    <use href="#fr"/><text x="5" y="8" class="st">OUR AGENDA</text>
    <text x="26" y="44" text-anchor="middle" class="brand" style="font-size:7px">NORVANE</text>
    <g fill="#1a4b9f"><circle cx="52" cy="22" r="3"/><circle cx="52" cy="32" r="3"/><circle cx="52" cy="42" r="3"/><circle cx="52" cy="52" r="3"/><circle cx="52" cy="62" r="3"/></g>
    <g fill="#8a8f99"><rect x="58" y="20" width="28" height="4"/><rect x="58" y="30" width="28" height="4"/><rect x="58" y="40" width="28" height="4"/><rect x="58" y="50" width="28" height="4"/><rect x="58" y="60" width="28" height="4"/></g>
    <text x="92" y="23" class="sx">Describe item here</text><text x="92" y="33" class="sx">Describe item here</text><text x="92" y="43" class="sx">Describe item here</text><text x="92" y="53" class="sx">Describe item here</text><text x="92" y="63" class="sx">Describe item here</text>
  </svg>
  <svg class="slide lg" style="left:398px;top:860px" viewBox="0 0 144 82">
    <use href="#fr"/><text x="5" y="8" class="st">TABLE OF CONTENTS</text>
    <g fill="#1a4b9f"><circle cx="14" cy="24" r="3.5"/><circle cx="60" cy="24" r="3.5"/><circle cx="106" cy="24" r="3.5"/><circle cx="14" cy="44" r="3.5"/><circle cx="60" cy="44" r="3.5"/><circle cx="106" cy="44" r="3.5"/><circle cx="14" cy="64" r="3.5"/><circle cx="60" cy="64" r="3.5"/><circle cx="106" cy="64" r="3.5"/></g>
    <text x="20" y="25" class="sh">Title Here</text><text x="66" y="25" class="sh">Title Here</text><text x="112" y="25" class="sh">Title Here</text>
    <text x="20" y="45" class="sh">Title Here</text><text x="66" y="45" class="sh">Title Here</text><text x="112" y="45" class="sh">Title Here</text>
    <text x="20" y="65" class="sh">Title Here</text><text x="66" y="65" class="sh">Title Here</text><text x="112" y="65" class="sh">Title Here</text>
  </svg>

  <svg class="slide lg" style="left:54px;top:954px" viewBox="0 0 144 82">
    <use href="#fr"/><text x="5" y="8" class="st">ICON SLIDE IDEA</text>
    <g fill="#1a4b9f"><circle cx="14" cy="24" r="4"/><circle cx="14" cy="44" r="4"/><circle cx="14" cy="64" r="4"/><circle cx="80" cy="24" r="4"/><circle cx="80" cy="44" r="4"/><circle cx="80" cy="64" r="4"/></g>
    <text x="22" y="23" class="sh">Title Goes Here</text><text x="22" y="27" class="sx">Short supporting line</text>
    <text x="22" y="43" class="sh">Title Goes Here</text><text x="22" y="47" class="sx">Short supporting line</text>
    <text x="22" y="63" class="sh">Title Goes Here</text><text x="22" y="67" class="sx">Short supporting line</text>
    <text x="88" y="23" class="sh">Title Goes Here</text><text x="88" y="43" class="sh">Title Goes Here</text><text x="88" y="63" class="sh">Title Goes Here</text>
  </svg>
  <svg class="slide lg" style="left:226px;top:954px" viewBox="0 0 144 82">
    <use href="#fr"/><text x="5" y="8" class="st">FULL SLIDE TEXT</text>
    <text x="6" y="18" class="sx">Lorem ipsum dolor sit amet, consectetur adipiscing elit, sed do eiusmod tempor incididunt ut labore.</text>
    <text x="6" y="23" class="sx">Et dolore magna aliqua. Ut enim ad minim veniam, quis nostrud exercitation ullamco laboris nisi.</text>
    <text x="6" y="28" class="sx">Ut aliquip ex ea commodo consequat. Duis aute irure dolor in reprehenderit in voluptate velit.</text>
    <text x="6" y="38" class="sx">Esse cillum dolore eu fugiat nulla pariatur. Excepteur sint occaecat cupidatat non proident.</text>
    <text x="6" y="43" class="sx">Sunt in culpa qui officia deserunt mollit anim id est laborum sed ut perspiciatis.</text>
    <text x="6" y="53" class="sx">Unde omnis iste natus error sit voluptatem accusantium doloremque laudantium totam.</text>
  </svg>
  <svg class="slide lg" style="left:398px;top:954px" viewBox="0 0 144 82">
    <use href="#fr"/><text x="5" y="8" class="st">2 COLUMNS TEXT SLIDE</text>
    <text x="6" y="18" class="sh">ENTER YOUR HEADING HERE</text><text x="76" y="18" class="sh">ENTER YOUR HEADING HERE</text>
    <text x="6" y="24" class="sx">Lorem ipsum dolor sit amet consectetur.</text><text x="76" y="24" class="sx">Lorem ipsum dolor sit amet consectetur.</text>
    <text x="6" y="29" class="sx">Sed do eiusmod tempor incididunt ut.</text><text x="76" y="29" class="sx">Sed do eiusmod tempor incididunt ut.</text>
    <text x="6" y="34" class="sx">Labore et dolore magna aliqua enim.</text><text x="76" y="34" class="sx">Labore et dolore magna aliqua enim.</text>
    <text x="6" y="44" class="sx">Quis nostrud exercitation ullamco.</text><text x="76" y="44" class="sx">Quis nostrud exercitation ullamco.</text>
  </svg>

  <svg class="slide lg" style="left:54px;top:1050px" viewBox="0 0 144 82">
    <use href="#fr"/><text x="5" y="8" class="st">YOUR SLIDE TITLE HERE</text>
    <rect x="0" y="16" width="144" height="36" fill="#1a4b9f"/>
    <rect x="0" y="16" width="70" height="36" fill="url(#gPhoto)" role="img" aria-label="Machine shop photo"/>
    <text x="82" y="30" class="shw">"If you don't know where you</text>
    <text x="82" y="35" class="shw">are going, you'll end up</text>
    <text x="82" y="40" class="shw">someplace else."</text>
    <text x="6" y="60" class="sx">Lorem ipsum dolor sit amet consectetur.</text><text x="76" y="60" class="sx">Lorem ipsum dolor sit amet consectetur.</text>
  </svg>
  <svg class="slide lg" style="left:226px;top:1050px" viewBox="0 0 144 82">
    <use href="#fr"/><text x="5" y="8" class="st">YOUR SLIDE TITLE HERE</text>
    <rect x="0" y="16" width="144" height="60" fill="#1a4b9f"/>
    <rect x="0" y="16" width="60" height="60" fill="url(#gPhoto)" role="img" aria-label="Engine component photo"/>
    <g fill="#fff"><circle cx="72" cy="28" r="3"/><circle cx="104" cy="28" r="3"/><circle cx="72" cy="52" r="3"/><circle cx="104" cy="52" r="3"/></g>
    <text x="78" y="29" class="shw">Title Here</text><text x="110" y="29" class="shw">Title Here</text><text x="78" y="53" class="shw">Title Here</text><text x="110" y="53" class="shw">Title Here</text>
  </svg>
  <svg class="slide lg" style="left:398px;top:1050px" viewBox="0 0 144 82">
    <use href="#fr"/><text x="5" y="8" class="st">YOUR SLIDE TITLE HERE</text>
    <text x="6" y="17" class="sx">Lorem ipsum dolor sit amet consectetur adipiscing.</text>
    <g fill="#1a4b9f"><rect x="6" y="26" width="16" height="14"/><rect x="42" y="26" width="16" height="14"/><rect x="24" y="42" width="16" height="14"/><rect x="60" y="42" width="16" height="14"/></g>
    <g fill="#8a8f99"><rect x="24" y="26" width="16" height="14"/><rect x="60" y="26" width="16" height="14"/><rect x="6" y="42" width="16" height="14"/><rect x="42" y="42" width="16" height="14"/></g>
    <rect x="84" y="14" width="60" height="62" fill="url(#gSteel)" role="img" aria-label="Office building photo"/>
  </svg>

  <div class="cont">cont.</div>
  <svg class="cont-arrow" width="34" height="26" viewBox="0 0 34 26" aria-hidden="true">
    <path d="M0 7 H18 V0 L34 13 L18 26 V19 H0 Z" fill="#c8b29c"/>
  </svg>

  <!-- continued layouts: column 1 -->
  <svg class="slide" style="left:666px;top:42px" viewBox="0 0 144 82">
    <use href="#fr"/><text x="5" y="8" class="st">YOUR SLIDE TITLE HERE</text>
    <rect x="72" y="0" width="72" height="79" fill="url(#gWarm)" role="img" aria-label="Heavy truck photo"/>
    <g fill="#1a4b9f"><circle cx="10" cy="22" r="2.5"/><circle cx="10" cy="34" r="2.5"/><circle cx="10" cy="46" r="2.5"/><circle cx="10" cy="58" r="2.5"/></g>
    <text x="16" y="23" class="sh">Title Goes Here</text><text x="16" y="35" class="sh">Title Goes Here</text><text x="16" y="47" class="sh">Title Goes Here</text><text x="16" y="59" class="sh">Title Goes Here</text>
  </svg>
  <svg class="slide" style="left:666px;top:134px" viewBox="0 0 144 82">
    <use href="#fr"/><text x="5" y="8" class="st">YOUR SLIDE TITLE HERE</text>
    <text x="5" y="15" class="sx">Lorem ipsum dolor sit amet consectetur adipiscing elit.</text>
    <rect x="0" y="24" width="64" height="30" fill="url(#gPhoto)" role="img" aria-label="Machined parts photo"/>
    <rect x="64" y="24" width="80" height="30" fill="#1a4b9f"/>
    <text x="70" y="34" class="sxw">Lorem ipsum dolor sit amet consectetur.</text>
    <text x="70" y="39" class="sxw">Sed do eiusmod tempor incididunt.</text>
    <text x="5" y="62" class="sx">Lorem ipsum dolor sit amet.</text>
  </svg>
  <svg class="slide" style="left:666px;top:229px" viewBox="0 0 144 82">
    <use href="#fr"/><text x="5" y="8" class="st">ICONS SLIDE IDEA</text>
    <g fill="none" stroke="#6d7280" stroke-width=".8"><rect x="10" y="26" width="8" height="6"/><circle cx="50" cy="29" r="4"/><rect x="88" y="26" width="8" height="6"/><circle cx="14" cy="54" r="4"/><rect x="46" y="51" width="8" height="6"/><circle cx="92" cy="54" r="4"/></g>
    <text x="22" y="30" class="sh">Title Here</text><text x="58" y="30" class="sh">Title Here</text><text x="100" y="30" class="sh">Title Here</text>
    <text x="22" y="55" class="sh">Title Here</text><text x="58" y="55" class="sh">Title Here</text><text x="100" y="55" class="sh">Title Here</text>
  </svg>
  <svg class="slide" style="left:666px;top:331px" viewBox="0 0 144 82">
    <use href="#fr"/><text x="5" y="8" class="st">YOUR SLIDE TITLE HERE</text>
    <rect x="10" y="18" width="24" height="26" fill="url(#gPhoto)" role="img" aria-label="Factory photo"/>
    <rect x="36" y="18" width="24" height="26" fill="url(#gWarm)" role="img" aria-label="Truck photo"/>
    <rect x="62" y="18" width="24" height="26" fill="url(#gPhoto)" role="img" aria-label="Robot arm photo"/>
    <rect x="10" y="46" width="24" height="24" fill="url(#gSteel)" role="img" aria-label="Gears photo"/>
    <rect x="36" y="46" width="24" height="24" fill="url(#gPhoto)" role="img" aria-label="Turbine photo"/>
    <rect x="62" y="46" width="24" height="24" fill="url(#gWarm)" role="img" aria-label="Welding photo"/>
    <text x="92" y="30" class="sx">Lorem ipsum dolor sit.</text><text x="92" y="35" class="sx">Consectetur adipiscing.</text>
  </svg>
  <svg class="slide" style="left:666px;top:424px" viewBox="0 0 144 82">
    <use href="#fr"/><text x="5" y="8" class="st">TABLE SLIDE IDEA</text>
    <rect x="6" y="14" width="132" height="5" fill="#1a4b9f"/>
    <g fill="#d5d9e3"><rect x="6" y="20" width="132" height="5"/><rect x="6" y="32" width="132" height="5"/><rect x="6" y="44" width="132" height="5"/><rect x="6" y="56" width="132" height="5"/><rect x="6" y="68" width="132" height="5"/></g>
    <g fill="#c2c8d6"><rect x="6" y="26" width="132" height="5"/><rect x="6" y="38" width="132" height="5"/><rect x="6" y="50" width="132" height="5"/><rect x="6" y="62" width="132" height="5"/></g>
    <text x="10" y="17.5" class="sxw">Column Title</text><text x="44" y="17.5" class="sxw">Column Title</text><text x="78" y="17.5" class="sxw">Column Title</text><text x="112" y="17.5" class="sxw">Column Title</text>
  </svg>
  <svg class="slide" style="left:666px;top:519px" viewBox="0 0 144 82">
    <use href="#fr"/><text x="5" y="8" class="st">YOUR SLIDE TITLE HERE</text>
    <circle cx="72" cy="44" r="18" fill="none" stroke="#1a4b9f" stroke-width="7" stroke-dasharray="12 3"/>
    <circle cx="72" cy="44" r="11" fill="#1a4b9f"/>
    <text x="72" y="45.5" text-anchor="middle" class="shw">NORVANE</text>
    <text x="10" y="24" class="sh">Title Here</text><text x="10" y="60" class="sh">Title Here</text><text x="104" y="24" class="sh">Title Here</text><text x="104" y="60" class="sh">Title Here</text>
  </svg>
  <svg class="slide" style="left:666px;top:618px" viewBox="0 0 144 82">
    <use href="#fr"/><text x="5" y="8" class="st">YOUR SLIDE TITLE HERE</text>
    <line x1="10" y1="44" x2="136" y2="44" stroke="#c9ccd3" stroke-width=".5"/>
    <g fill="#1a4b9f"><rect x="16" y="34" width="5" height="10"/><rect x="30" y="20" width="5" height="24"/><rect x="44" y="44" width="5" height="12"/><rect x="58" y="18" width="5" height="26"/><rect x="72" y="44" width="5" height="18"/><rect x="86" y="24" width="5" height="20"/><rect x="100" y="44" width="5" height="8"/><rect x="114" y="30" width="5" height="14"/><rect x="128" y="44" width="5" height="22"/></g>
  </svg>
  <svg class="slide" style="left:666px;top:711px" viewBox="0 0 144 82">
    <use href="#fr"/><text x="5" y="8" class="st">YOUR SLIDE TITLE HERE</text>
    <path d="M10 72 L10 50 L28 36 L46 46 L64 30 L82 44 L100 28 L118 40 L136 30 L136 72 Z" fill="#9bb0d6"/>
    <path d="M10 72 L10 58 L28 48 L46 56 L64 42 L82 54 L100 44 L118 52 L136 46 L136 72 Z" fill="#1a4b9f"/>
  </svg>
  <svg class="slide" style="left:666px;top:806px" viewBox="0 0 144 82">
    <use href="#fr"/>
    <rect x="0" y="0" width="42" height="79" fill="url(#gPhoto)" role="img" aria-label="Assembly line photo"/>
    <rect x="42" y="0" width="44" height="79" fill="#1a4b9f"/>
    <text x="48" y="16" class="sxw">Lorem ipsum dolor sit amet,</text>
    <text x="48" y="21" class="sxw">consectetur adipiscing elit.</text>
    <text x="48" y="26" class="sxw">Sed do eiusmod tempor.</text>
    <g fill="#1a4b9f"><circle cx="94" cy="30" r="2.5"/><circle cx="94" cy="42" r="2.5"/><circle cx="94" cy="54" r="2.5"/></g>
    <text x="99" y="31" class="sh">Title Here</text><text x="99" y="43" class="sh">Title Here</text><text x="99" y="55" class="sh">Title Here</text>
  </svg>
  <svg class="slide" style="left:666px;top:907px" viewBox="0 0 144 82">
    <use href="#fr"/><text x="5" y="8" class="st">YOUR SLIDE TITLE HERE</text>
    <text x="5" y="15" class="sx">Lorem ipsum dolor sit amet consectetur adipiscing elit sed do.</text>
    <rect x="8" y="26" width="30" height="20" fill="url(#gSteel)" role="img" aria-label="Light bulb photo"/>
    <rect x="40" y="26" width="30" height="20" fill="url(#gPhoto)" role="img" aria-label="Laptop photo"/>
    <rect x="72" y="26" width="30" height="20" fill="url(#gWarm)" role="img" aria-label="Meeting photo"/>
    <rect x="104" y="26" width="30" height="20" fill="url(#gPhoto)" role="img" aria-label="Office photo"/>
    <rect x="8" y="50" width="30" height="20" fill="url(#gPhoto)" role="img" aria-label="Workshop photo"/>
    <rect x="40" y="50" width="30" height="20" fill="url(#gSteel)" role="img" aria-label="Chart photo"/>
    <rect x="72" y="50" width="30" height="20" fill="url(#gPhoto)" role="img" aria-label="Team photo"/>
    <rect x="104" y="50" width="30" height="20" fill="url(#gWarm)" role="img" aria-label="Handshake photo"/>
  </svg>
  <svg class="slide" style="left:666px;top:1000px" viewBox="0 0 144 82">
    <use href="#fr"/><text x="5" y="8" class="st">YOUR SLIDE TITLE HERE</text>
    <path d="M40 16 A28 28 0 0 0 40 72" fill="none" stroke="#1a4b9f" stroke-width="1.2"/>
    <text x="24" y="46" text-anchor="middle" class="brand" style="font-size:6px">NORVANE</text>
    <g fill="#1a4b9f"><circle cx="60" cy="22" r="2.5"/><circle cx="64" cy="34" r="2.5"/><circle cx="64" cy="48" r="2.5"/><circle cx="60" cy="62" r="2.5"/></g>
    <text x="66" y="23" class="sh">Title Here</text><text x="70" y="35" class="sh">Title Here</text><text x="70" y="49" class="sh">Title Here</text><text x="66" y="63" class="sh">Title Here</text>
    <text x="104" y="24" class="sx">Lorem ipsum dolor</text><text x="104" y="29" class="sx">sit amet consectetur.</text>
  </svg>
  <svg class="slide" style="left:666px;top:1095px" viewBox="0 0 144 82">
    <use href="#fr"/><text x="5" y="8" class="st">YOUR SLIDE TITLE HERE</text>
    <g transform="translate(72 44)">
      <rect x="-20" y="-10" width="14" height="14" transform="rotate(45 -13 -3)" fill="#8a8f99"/>
      <rect x="6" y="-10" width="14" height="14" transform="rotate(45 13 -3)" fill="#1a4b9f"/>
      <rect x="-20" y="10" width="14" height="14" transform="rotate(45 -13 17)" fill="#1a4b9f"/>
      <rect x="6" y="10" width="14" height="14" transform="rotate(45 13 17)" fill="#8a8f99"/>
    </g>
    <text x="10" y="26" class="sh">Title Here</text><text x="10" y="62" class="sh">Title Here</text><text x="106" y="26" class="sh">Title Here</text><text x="106" y="62" class="sh">Title Here</text>
  </svg>

  <!-- column 2 -->
  <svg class="slide" style="left:834px;top:42px" viewBox="0 0 144 82">
    <use href="#fr"/>
    <rect x="0" y="0" width="66" height="79" fill="url(#gWarm)" role="img" aria-label="Robotic welding line photo"/>
    <g fill="#1a4b9f"><circle cx="76" cy="20" r="2.5"/><circle cx="76" cy="34" r="2.5"/><circle cx="76" cy="48" r="2.5"/><circle cx="76" cy="62" r="2.5"/></g>
    <text x="82" y="21" class="sh">Title Goes Here</text><text x="82" y="35" class="sh">Title Goes Here</text><text x="82" y="49" class="sh">Title Goes Here</text><text x="82" y="63" class="sh">Title Goes Here</text>
  </svg>
  <svg class="slide" style="left:834px;top:134px" viewBox="0 0 144 82">
    <use href="#fr"/><text x="5" y="8" class="st">YOUR SLIDE TITLE HERE</text>
    <rect x="0" y="22" width="144" height="30" fill="url(#gPhoto)" role="img" aria-label="Pipework plant photo"/>
    <g fill="#1a4b9f"><circle cx="20" cy="58" r="5"/><circle cx="56" cy="58" r="5"/><circle cx="92" cy="58" r="5"/><circle cx="128" cy="58" r="5"/></g>
    <text x="20" y="70" text-anchor="middle" class="sh">Title Here</text><text x="56" y="70" text-anchor="middle" class="sh">Title Here</text><text x="92" y="70" text-anchor="middle" class="sh">Title Here</text><text x="128" y="70" text-anchor="middle" class="sh">Title Here</text>
  </svg>
  <svg class="slide" style="left:834px;top:229px" viewBox="0 0 144 82">
    <use href="#fr"/><text x="5" y="8" class="st">TIMELINE SLIDE IDEA</text>
    <g fill="#8a8f99"><path d="M8 40 h20 l4 4 l-4 4 h-20 z"/><path d="M60 40 h20 l4 4 l-4 4 h-20 z"/><path d="M112 40 h20 l4 4 l-4 4 h-20 z"/></g>
    <g fill="#1a4b9f"><path d="M34 40 h20 l4 4 l-4 4 h-20 z"/><path d="M86 40 h20 l4 4 l-4 4 h-20 z"/></g>
    <text x="12" y="26" class="sx">2012 Lorem</text><text x="64" y="26" class="sx">2014 Lorem</text><text x="116" y="26" class="sx">2016 Lorem</text>
    <text x="38" y="60" class="sx">2013 Ipsum</text><text x="90" y="60" class="sx">2015 Ipsum</text>
  </svg>
  <svg class="slide" style="left:834px;top:331px" viewBox="0 0 144 82">
    <use href="#fr"/><text x="5" y="8" class="st">YOUR SLIDE TITLE HERE</text>
    <rect x="8" y="16" width="40" height="24" fill="#1a4b9f"/>
    <text x="12" y="24" class="shw">Your Text Here</text>
    <rect x="8" y="42" width="40" height="28" fill="url(#gPhoto)" role="img" aria-label="Factory floor photo"/>
    <rect x="50" y="16" width="40" height="54" fill="url(#gWarm)" role="img" aria-label="Workshop photo"/>
    <rect x="92" y="16" width="44" height="54" fill="url(#gSteel)" role="img" aria-label="Engine closeup photo"/>
  </svg>
  <svg class="slide" style="left:834px;top:424px" viewBox="0 0 144 82">
    <use href="#fr"/><text x="5" y="8" class="st">YOUR SLIDE TITLE HERE</text>
    <text x="72" y="17" text-anchor="middle" class="sx">Chart Title</text>
    <g fill="#1a4b9f"><rect x="18" y="38" width="6" height="30"/><rect x="48" y="46" width="6" height="22"/><rect x="78" y="42" width="6" height="26"/><rect x="108" y="34" width="6" height="34"/></g>
    <g fill="#8a8f99"><rect x="25" y="48" width="6" height="20"/><rect x="55" y="38" width="6" height="30"/><rect x="85" y="50" width="6" height="18"/><rect x="115" y="44" width="6" height="24"/></g>
    <line x1="12" y1="68" x2="132" y2="68" stroke="#8a8f99" stroke-width=".4"/>
  </svg>
  <svg class="slide" style="left:834px;top:519px" viewBox="0 0 144 82">
    <use href="#fr"/><text x="5" y="8" class="st">YOUR SLIDE TITLE HERE</text>
    <g fill="#1a4b9f"><rect x="14" y="40" width="4" height="28"/><rect x="30" y="34" width="4" height="34"/><rect x="46" y="44" width="4" height="24"/><rect x="62" y="28" width="4" height="40"/><rect x="78" y="36" width="4" height="32"/><rect x="94" y="22" width="4" height="46"/><rect x="110" y="38" width="4" height="30"/><rect x="126" y="30" width="4" height="38"/></g>
    <g fill="#8a8f99"><rect x="19" y="48" width="4" height="20"/><rect x="35" y="44" width="4" height="24"/><rect x="51" y="40" width="4" height="28"/><rect x="67" y="46" width="4" height="22"/><rect x="83" y="42" width="4" height="26"/><rect x="99" y="50" width="4" height="18"/><rect x="115" y="44" width="4" height="24"/><rect x="131" y="48" width="4" height="20"/></g>
  </svg>
  <svg class="slide" style="left:834px;top:618px" viewBox="0 0 144 82">
    <use href="#fr"/><text x="5" y="8" class="st">YOUR SLIDE TITLE HERE</text>
    <polyline points="12,50 28,36 44,44 60,28 76,40 92,30 108,46 124,34 136,38" fill="none" stroke="#1a4b9f" stroke-width=".8"/>
    <polyline points="12,60 28,54 44,58 60,46 76,56 92,50 108,54 124,44 136,52" fill="none" stroke="#8a8f99" stroke-width=".8"/>
    <polyline points="12,40 28,48 44,34 60,52 76,30 92,44 108,36 124,56 136,42" fill="none" stroke="#9bb0d6" stroke-width=".8"/>
  </svg>
  <svg class="slide" style="left:834px;top:711px" viewBox="0 0 144 82">
    <rect width="144" height="82" fill="url(#gSteel)" role="img" aria-label="Engine gears photo"/>
    <circle cx="72" cy="41" r="20" fill="#1a4b9f"/>
    <text x="72" y="40" text-anchor="middle" class="stw">SECTION</text>
    <text x="72" y="46" text-anchor="middle" class="stw">BREAK</text>
  </svg>
  <svg class="slide" style="left:834px;top:806px" viewBox="0 0 144 82">
    <rect width="144" height="82" fill="#1a4b9f"/>
    <text x="72" y="9" text-anchor="middle" class="stw">YOUR SLIDE TITLE HERE</text>
    <g fill="#8a8f99"><rect x="10" y="22" width="36" height="44"/><rect x="54" y="22" width="36" height="44"/><rect x="98" y="22" width="36" height="44"/></g>
    <text x="28" y="50" text-anchor="middle" class="shw">Title Here</text><text x="72" y="50" text-anchor="middle" class="shw">Title Here</text><text x="116" y="50" text-anchor="middle" class="shw">Title Here</text>
  </svg>
  <svg class="slide" style="left:834px;top:907px" viewBox="0 0 144 82">
    <use href="#fr"/><text x="5" y="8" class="st">YOUR SLIDE TITLE HERE</text>
    <rect x="10" y="52" width="20" height="10" fill="#8a8f99"/><rect x="32" y="44" width="20" height="10" fill="#6d7280"/><rect x="54" y="36" width="20" height="10" fill="#1a4b9f"/><rect x="76" y="28" width="20" height="10" fill="#6d7280"/><rect x="98" y="20" width="20" height="10" fill="#1a4b9f"/>
    <text x="100" y="40" class="sx">Title Goes Here</text>
    <circle cx="103" cy="66" r="2.5" fill="#1a4b9f"/><text x="108" y="67" class="sh">Title Here</text>
  </svg>
  <svg class="slide" style="left:834px;top:1000px" viewBox="0 0 144 82">
    <use href="#fr"/><text x="5" y="8" class="st">YOUR SLIDE TITLE HERE</text>
    <circle cx="22" cy="38" r="12" fill="#1a4b9f"/><circle cx="44" cy="38" r="12" fill="#8a8f99"/><circle cx="66" cy="38" r="12" fill="#1a4b9f"/><circle cx="88" cy="38" r="12" fill="#8a8f99"/><circle cx="110" cy="38" r="12" fill="#9bb0d6"/>
    <text x="22" y="60" text-anchor="middle" class="sh">Title</text><text x="44" y="60" text-anchor="middle" class="sh">Title</text><text x="66" y="60" text-anchor="middle" class="sh">Title</text><text x="88" y="60" text-anchor="middle" class="sh">Title</text><text x="110" y="60" text-anchor="middle" class="sh">Title</text>
  </svg>
  <svg class="slide" style="left:834px;top:1095px" viewBox="0 0 144 82">
    <use href="#fr"/><text x="5" y="8" class="st">YOUR SLIDE TITLE HERE</text>
    <g fill="#6d7280"><rect x="46" y="26" width="12" height="36"/><rect x="86" y="26" width="12" height="36"/></g>
    <g fill="#9bb0d6"><rect x="58" y="20" width="12" height="44"/><rect x="74" y="20" width="12" height="44"/></g>
    <text x="12" y="30" class="sh">Title Here</text><text x="110" y="30" class="sh">Title Here</text><text x="12" y="60" class="sh">Title Here</text><text x="110" y="60" class="sh">Title Here</text>
  </svg>

  <!-- column 3 -->
  <svg class="slide" style="left:1002px;top:42px" viewBox="0 0 144 82">
    <use href="#fr"/>
    <rect x="0" y="0" width="144" height="22" fill="#2f5e94"/>
    <text x="72" y="8" text-anchor="middle" class="stw">YOUR SLIDE TITLE HERE</text>
    <text x="72" y="15" text-anchor="middle" class="sxw">Lorem ipsum dolor sit amet consectetur adipiscing.</text>
    <g fill="#1a4b9f"><circle cx="16" cy="38" r="4"/><circle cx="60" cy="38" r="4"/><circle cx="104" cy="38" r="4"/></g>
    <g fill="#8a8f99"><circle cx="16" cy="58" r="4"/><circle cx="60" cy="58" r="4"/><circle cx="104" cy="58" r="4"/></g>
    <text x="24" y="39" class="sh">Title Here</text><text x="68" y="39" class="sh">Title Here</text><text x="112" y="39" class="sh">Title Here</text>
    <text x="24" y="59" class="sh">Title Here</text><text x="68" y="59" class="sh">Title Here</text><text x="112" y="59" class="sh">Title Here</text>
  </svg>
  <svg class="slide" style="left:1002px;top:134px" viewBox="0 0 144 82">
    <use href="#fr"/>
    <rect x="0" y="0" width="68" height="79" fill="url(#gPhoto)" role="img" aria-label="Precision machine spindle photo"/>
    <rect x="68" y="0" width="76" height="12" fill="#eef0f6"/>
    <text x="78" y="8" class="st">YOUR SLIDE TITLE</text>
    <g fill="#8a8f99"><circle cx="76" cy="22" r="2.5"/><circle cx="76" cy="36" r="2.5"/><circle cx="76" cy="50" r="2.5"/><circle cx="76" cy="64" r="2.5"/></g>
    <text x="82" y="23" class="sh">Title Goes Here</text><text x="82" y="37" class="sh">Title Goes Here</text><text x="82" y="51" class="sh">Title Goes Here</text><text x="82" y="65" class="sh">Title Goes Here</text>
  </svg>
  <svg class="slide" style="left:1002px;top:229px" viewBox="0 0 144 82">
    <use href="#fr"/><text x="5" y="8" class="st">TEAM MEMBERS</text>
    <rect x="12" y="20" width="24" height="30" fill="url(#gSteel)" role="img" aria-label="Team member portrait"/>
    <rect x="44" y="20" width="24" height="30" fill="url(#gSteel)" role="img" aria-label="Team member portrait"/>
    <rect x="76" y="20" width="24" height="30" fill="url(#gSteel)" role="img" aria-label="Team member portrait"/>
    <rect x="108" y="20" width="24" height="30" fill="url(#gSteel)" role="img" aria-label="Team member portrait"/>
    <text x="24" y="56" text-anchor="middle" class="sh">Name Here</text><text x="56" y="56" text-anchor="middle" class="sh">Name Here</text><text x="88" y="56" text-anchor="middle" class="sh">Name Here</text><text x="120" y="56" text-anchor="middle" class="sh">Name Here</text>
    <text x="24" y="61" text-anchor="middle" class="sx">Position</text><text x="56" y="61" text-anchor="middle" class="sx">Position</text><text x="88" y="61" text-anchor="middle" class="sx">Position</text><text x="120" y="61" text-anchor="middle" class="sx">Position</text>
  </svg>
  <svg class="slide" style="left:1002px;top:331px" viewBox="0 0 144 82">
    <use href="#fr"/><text x="5" y="8" class="st">YOUR SLIDE TITLE HERE</text>
    <rect x="8" y="18" width="36" height="54" fill="url(#gWarm)" role="img" aria-label="Delivery truck photo"/>
    <rect x="46" y="18" width="30" height="54" fill="#8a8f99"/>
    <rect x="78" y="18" width="30" height="54" fill="url(#gPhoto)" role="img" aria-label="Factory photo"/>
    <rect x="110" y="18" width="28" height="54" fill="url(#gWarm)" role="img" aria-label="Production line photo"/>
    <text x="50" y="46" class="shw">Title Here</text>
  </svg>
  <svg class="slide" style="left:1002px;top:424px" viewBox="0 0 144 82">
    <use href="#fr"/><text x="5" y="8" class="st">YOUR SLIDE TITLE HERE</text>
    <text x="30" y="20" text-anchor="middle" class="sx">Sales</text>
    <ellipse cx="30" cy="44" rx="22" ry="13" fill="#8a8f99"/>
    <path d="M30 44 L30 31 A22 13 0 1 1 8 44 Z" fill="#1a4b9f"/>
    <g fill="#1a4b9f"><circle cx="78" cy="30" r="2.2"/><circle cx="78" cy="42" r="2.2"/><circle cx="78" cy="54" r="2.2"/><circle cx="78" cy="66" r="2.2"/></g>
    <text x="84" y="31" class="sh">Title Goes Here</text><text x="84" y="43" class="sh">Title Goes Here</text><text x="84" y="55" class="sh">Title Goes Here</text><text x="84" y="67" class="sh">Title Goes Here</text>
  </svg>
  <svg class="slide" style="left:1002px;top:519px" viewBox="0 0 144 82">
    <use href="#fr"/><text x="5" y="8" class="st">YOUR SLIDE TITLE HERE</text>
    <text x="5" y="15" class="sx">Lorem ipsum dolor sit amet consectetur adipiscing elit.</text>
    <g fill="none" stroke-width="1.2"><circle cx="20" cy="44" r="11" stroke="#1a4b9f"/><circle cx="54" cy="44" r="11" stroke="#8a8f99"/><circle cx="88" cy="44" r="11" stroke="#1a4b9f"/><circle cx="122" cy="44" r="11" stroke="#8a8f99"/></g>
    <text x="20" y="46" text-anchor="middle" class="sh">65:35</text><text x="54" y="46" text-anchor="middle" class="sh">20:80</text><text x="88" y="46" text-anchor="middle" class="sh">65:35</text><text x="122" y="46" text-anchor="middle" class="sh">20:80</text>
  </svg>
  <svg class="slide" style="left:1002px;top:618px" viewBox="0 0 144 82">
    <use href="#fr"/><text x="5" y="8" class="st">COMPARATIVE HISTOGRAM CHART</text>
    <g fill="#8a8f99"><rect x="56" y="20" width="16" height="4"/><rect x="44" y="26" width="28" height="4"/><rect x="34" y="32" width="38" height="4"/><rect x="24" y="38" width="48" height="4"/><rect x="36" y="44" width="36" height="4"/><rect x="48" y="50" width="24" height="4"/><rect x="58" y="56" width="14" height="4"/></g>
    <g fill="#1a4b9f"><rect x="72" y="20" width="20" height="4"/><rect x="72" y="26" width="32" height="4"/><rect x="72" y="32" width="44" height="4"/><rect x="72" y="38" width="54" height="4"/><rect x="72" y="44" width="40" height="4"/><rect x="72" y="50" width="26" height="4"/><rect x="72" y="56" width="12" height="4"/></g>
  </svg>
  <svg class="slide" style="left:1002px;top:711px" viewBox="0 0 144 82">
    <use href="#fr"/><text x="5" y="8" class="st">YOUR SLIDE TITLE HERE</text>
    <text x="5" y="15" class="sx">Lorem ipsum dolor sit amet consectetur adipiscing elit sed do.</text>
    <g fill="#6d7280"><rect x="18" y="34" width="6" height="6"/><rect x="50" y="34" width="6" height="6"/><circle cx="88" cy="37" r="3"/><rect x="116" y="34" width="6" height="6"/></g>
    <text x="21" y="50" text-anchor="middle" class="sh">Title Here</text><text x="53" y="50" text-anchor="middle" class="sh">Title Here</text><text x="88" y="50" text-anchor="middle" class="sh">Title Here</text><text x="119" y="50" text-anchor="middle" class="sh">Title Here</text>
  </svg>
  <svg class="slide" style="left:1002px;top:806px" viewBox="0 0 144 82">
    <use href="#fr"/>
    <rect x="0" y="0" width="144" height="56" fill="#1a4b9f"/>
    <rect x="0" y="0" width="48" height="28" fill="url(#gPhoto)" role="img" aria-label="Robot arm photo"/>
    <rect x="48" y="28" width="48" height="28" fill="url(#gWarm)" role="img" aria-label="Machining photo"/>
    <rect x="96" y="0" width="48" height="28" fill="url(#gPhoto)" role="img" aria-label="Factory photo"/>
    <text x="56" y="14" class="shw">Title Here</text><text x="8" y="44" class="shw">Title Here</text><text x="104" y="44" class="shw">Title Here</text>
    <text x="72" y="68" text-anchor="middle" class="st">YOUR SLIDE TITLE HERE</text>
  </svg>
  <svg class="slide" style="left:1002px;top:907px" viewBox="0 0 144 82">
    <use href="#fr"/><text x="5" y="8" class="st">YOUR SLIDE TITLE HERE</text>
    <circle cx="36" cy="46" r="24" fill="#d5d9e3"/>
    <path d="M36 46 L36 22 A24 24 0 0 1 58 54 Z" fill="#1a4b9f"/>
    <path d="M36 46 L58 54 A24 24 0 0 1 30 69 Z" fill="#8a8f99"/>
    <circle cx="36" cy="46" r="8" fill="#eef0f6"/>
    <text x="36" y="47.5" text-anchor="middle" class="sh" style="fill:#1a4b9f">NORVANE</text>
    <text x="72" y="28" class="sx">Lorem ipsum dolor sit amet consectetur.</text>
    <text x="72" y="42" class="sx">Sed do eiusmod tempor incididunt ut.</text>
    <text x="72" y="56" class="sx">Labore et dolore magna aliqua enim.</text>
  </svg>
  <svg class="slide" style="left:1002px;top:1000px" viewBox="0 0 144 82">
    <use href="#fr"/><text x="5" y="8" class="st">YOUR SLIDE TITLE HERE</text>
    <text x="5" y="15" class="sx">Lorem ipsum dolor sit amet consectetur adipiscing elit.</text>
    <path d="M14 40 A12 12 0 0 1 38 40 A12 12 0 0 0 62 40 A12 12 0 0 1 86 40 A12 12 0 0 0 110 40 A12 12 0 0 1 134 40" fill="none" stroke="#1a4b9f" stroke-width="2.5"/>
    <text x="26" y="60" text-anchor="middle" class="sh">Title</text><text x="50" y="60" text-anchor="middle" class="sh">Title</text><text x="74" y="60" text-anchor="middle" class="sh">Title</text><text x="98" y="60" text-anchor="middle" class="sh">Title</text><text x="122" y="60" text-anchor="middle" class="sh">Title</text>
  </svg>
  <svg class="slide" style="left:1002px;top:1095px" viewBox="0 0 144 82">
    <rect width="144" height="82" fill="url(#gCover)" role="img" aria-label="Blue plant interior photo"/>
    <text x="40" y="44" text-anchor="middle" class="stw">THANK YOU</text>
    <circle cx="104" cy="42" r="22" fill="#fff"/>
    <text x="104" y="44" text-anchor="middle" class="brand" style="font-size:7px">NORVANE</text>
  </svg>

</main>
</body>
</html>
```